Blueprints For A Steady Home Book*

Our book is about using engineering and biblical principles to solve problems in marriage. We are the wedlock Architects. See our branded logo in the attachments. We would like to see different types of graphics that shows continuous improvement in marriage. Our colors should be Gold Black and Red. Could use white text and symbols if needed. Brief description on the back with some quotes and our Picture. Use 5.5x8.5 as the size of the book. Not sure about the spine size.

Target Market(s)

Married couples

Font styles to use
Serif

Colors

Designer to choose colors to be used in the design.

Requirements
Nice to have
• Engineering symbols and Logos.

```html
<!DOCTYPE html>
<html lang="en">
<head>
<meta charset="utf-8">
<title>Blueprints For A Steady Home — Book Cover</title>
<link rel="stylesheet" href="https://fonts.googleapis.com/css2?family=Londrina+Solid:wght@400;900&family=Tinos:ital@0;1&display=swap">
<style>
  :root {
    --board-center: #2b3347;
    --board-mid: #222a3c;
    --board-edge: #151a27;
    --chalk: #ffffff;
    --heart-red: #e3100f;
    --heart-deep: #b10d0e;
    --gold: #c9a23a;
  }
  html, body {
    margin: 0;
    padding: 0;
    overflow: hidden;
    background: var(--board-edge);
  }
  .cover {
    position: relative;
    width: 848px;
    height: 1200px;
    overflow: hidden;
    background: radial-gradient(ellipse at 50% 40%, var(--board-center) 0%, var(--board-mid) 55%, var(--board-edge) 100%);
  }
  .cover-art {
    position: absolute;
    inset: 0;
    width: 848px;
    height: 1200px;
  }
  .brand-name {
    font-family: "Tinos", serif;
    font-size: 20px;
    letter-spacing: 1px;
    fill: var(--gold);
  }
  .brand-dot { fill: var(--gold); }
  .title-line {
    font-family: "Londrina Solid", sans-serif;
    font-weight: 900;
    fill: var(--chalk);
  }
  .axis { stroke: var(--chalk); stroke-width: 1.2; }
  .tick { stroke: var(--chalk); stroke-width: 1; }
  .axis-label, .tick-label {
    font-family: "Tinos", serif;
    font-style: italic;
    fill: var(--chalk);
  }
  .axis-label { font-size: 26px; }
  .tick-label { font-size: 19px; }
  .equation {
    position: absolute;
    left: 0;
    right: 0;
    top: 1040px;
    text-align: center;
    font-family: "Tinos", serif;
    font-style: italic;
    font-size: 42px;
    color: var(--chalk);
    line-height: 1;
    white-space: nowrap;
  }
  .equation .exp {
    font-size: 24px;
    vertical-align: 0.75em;
    margin-left: 1px;
  }
  .equation .op { font-style: normal; margin: 0 3px; }
  .equation .paren {
    font-style: normal;
    font-weight: 300;
    font-size: 58px;
    vertical-align: -0.08em;
    margin: 0 4px;
  }
  .equation .fraction {
    display: inline-block;
    vertical-align: middle;
    text-align: center;
    margin: 0 3px;
  }
  .equation .numerator {
    display: block;
    border-bottom: 1.5px solid var(--chalk);
    padding: 0 3px 3px;
  }
  .equation .denominator { display: block; padding-top: 4px; }
  .equation .radical { font-style: normal; margin-left: 2px; }
  .equation .radicand {
    border-top: 1.5px solid var(--chalk);
    padding: 2px 2px 0;
    font-size: 34px;
  }
  .equation .paren-exp {
    font-size: 24px;
    vertical-align: 1.2em;
  }
</style>
</head>
<body>
<main class="cover">
  <svg class="cover-art" viewBox="0 0 848 1200" xmlns="http://www.w3.org/2000/svg">
    <defs>
      <radialGradient id="heart-glow" cx="50%" cy="45%" r="55%">
        <stop offset="0%" stop-color="var(--heart-red)"/>
        <stop offset="70%" stop-color="var(--heart-deep)" stop-opacity="0.85"/>
        <stop offset="100%" stop-color="var(--heart-deep)" stop-opacity="0"/>
      </radialGradient>
    </defs>

    <g class="brand">
      <circle class="brand-dot" cx="424" cy="88" r="14"/>
      <text class="brand-name" x="424" y="150" text-anchor="middle">THE WEDLOCK ARCHITECTS</text>
    </g>

    <text class="title-line title-lead" x="206" y="217" font-size="56" textLength="436" lengthAdjust="spacingAndGlyphs">BLUEPRINTS FOR A</text>
    <text class="title-line title-main" x="115" y="387" font-size="196" textLength="624" lengthAdjust="spacingAndGlyphs">STEADY</text>
    <text class="title-line title-tail" x="193" y="502" font-size="122" textLength="459" lengthAdjust="spacingAndGlyphs">HOME</text>

    <rect class="heart-art" x="246" y="650" width="332" height="336" rx="60" fill="url(#heart-glow)"
          role="img" aria-label="Red chalk heart drawn over the graph axes"/>

    <g class="graph-axes">
      <line class="axis" x1="189" y1="842" x2="622" y2="842"/>
      <line class="axis" x1="409" y1="590" x2="409" y2="1027"/>

      <g class="x-ticks">
        <line class="tick" x1="219" y1="842" x2="219" y2="836"/>
        <line class="tick" x1="251" y1="842" x2="251" y2="834"/>
        <line class="tick" x1="282" y1="842" x2="282" y2="836"/>
        <line class="tick" x1="314" y1="842" x2="314" y2="836"/>
        <line class="tick" x1="330" y1="842" x2="330" y2="834"/>
        <line class="tick" x1="346" y1="842" x2="346" y2="836"/>
        <line class="tick" x1="377" y1="842" x2="377" y2="836"/>
        <line class="tick" x1="441" y1="842" x2="441" y2="836"/>
        <line class="tick" x1="472" y1="842" x2="472" y2="836"/>
        <line class="tick" x1="488" y1="842" x2="488" y2="834"/>
        <line class="tick" x1="504" y1="842" x2="504" y2="836"/>
        <line class="tick" x1="535" y1="842" x2="535" y2="836"/>
        <line class="tick" x1="567" y1="842" x2="567" y2="834"/>
        <line class="tick" x1="598" y1="842" x2="598" y2="836"/>
      </g>
      <g class="y-ticks">
        <line class="tick" x1="409" y1="598" x2="417" y2="598"/>
        <line class="tick" x1="409" y1="634" x2="415" y2="634"/>
        <line class="tick" x1="409" y1="666" x2="415" y2="666"/>
        <line class="tick" x1="409" y1="680" x2="417" y2="680"/>
        <line class="tick" x1="409" y1="698" x2="415" y2="698"/>
        <line class="tick" x1="409" y1="730" x2="415" y2="730"/>
        <line class="tick" x1="409" y1="762" x2="417" y2="762"/>
        <line class="tick" x1="409" y1="794" x2="415" y2="794"/>
        <line class="tick" x1="409" y1="826" x2="415" y2="826"/>
        <line class="tick" x1="409" y1="858" x2="415" y2="858"/>
        <line class="tick" x1="409" y1="890" x2="415" y2="890"/>
        <line class="tick" x1="409" y1="922" x2="417" y2="922"/>
        <line class="tick" x1="409" y1="954" x2="415" y2="954"/>
        <line class="tick" x1="409" y1="986" x2="415" y2="986"/>
        <line class="tick" x1="409" y1="1004" x2="417" y2="1004"/>
      </g>

      <text class="axis-label" x="404" y="580" text-anchor="middle">y</text>
      <text class="axis-label" x="637" y="850" text-anchor="middle">x</text>

      <text class="tick-label" x="403" y="604" text-anchor="end">1.5</text>
      <text class="tick-label" x="403" y="686" text-anchor="end">1.0</text>
      <text class="tick-label" x="403" y="768" text-anchor="end">0.5</text>
      <text class="tick-label" x="403" y="928" text-anchor="end">-0.5</text>
      <text class="tick-label" x="403" y="1010" text-anchor="end">-1.0</text>

      <text class="tick-label" x="251" y="864" text-anchor="middle">-1.0</text>
      <text class="tick-label" x="330" y="864" text-anchor="middle">-0.5</text>
      <text class="tick-label" x="488" y="864" text-anchor="middle">0.5</text>
      <text class="tick-label" x="567" y="864" text-anchor="middle">1.0</text>
    </g>
  </svg>

  <div class="equation" aria-label="x squared plus the quantity five y over four minus root of absolute x, squared, equals one">
    <span>x</span><span class="exp">2</span><span class="op">+</span><span class="paren">(</span><span class="fraction"><span class="numerator">5y</span><span class="denominator">4</span></span><span class="op">-</span><span class="radical">√</span><span class="radicand">|x|</span><span class="paren">)</span><span class="paren-exp">2</span><span class="op">=</span><span>1</span>
  </div>
</main>
</body>
</html>
```